Hourgala promotional materials

Hourgala is a Canada-wide event that matches non-profits to skilled volunteers. The first part of the evening, attendees mix and mingle with the non-profits in the room. The second half of the evening is a a silent art auction where attendees bid their time, not their money, on artwork that we have purchased from local emerging artists. A successful bid maxes out at 100 volunteer hours. The Art-Winner has twelve months to complete their pledge before taking their artwork home as a sign of their good will.

We are not looking for someone to design a promotional postcards that sums up and reflects what we do.

We would like to play off of our current logo and colour palate- does not have to be directly lifted, it can be an interpretive riff. We want our branding to be instantly recognizable.

Here is a link to a video about what we do: http://www.hourgala-events.ca/

Target Market(s)

Young professionals who are community minded and interested in cultural products. We skew female and 25-40.

Industry/Entity Type

Artists

Font styles to use
Sans Serif

Requirements
Must have
• a) Hourgala colours: Green #7ac044, Grey #3e3e40
b) Hourgala logo should always use the 3 colour EPS version

Link to the Hourgala Logo:
https://hourgala.filedrop-host.com/hourgalalogo
Nice to have
• We want it to be modern, clean, fun, easy to read. The Hourgala can be complex to explain, so simplicity is key. We are open to "riffs" on our logo. For example, if you want to take one aspect or theme expressed by our logo and incorporate it into the design, we'd be interested to see what you could come up with. Nothing too trendy and faddish please as we'd like to use these designs across several seasons.
Should not have
• We don't want overly engineered or complex designs that we can't adapt.

```html
<!DOCTYPE html>
<html lang="en">
<head>
<meta charset="utf-8">
<title>Hourgala – Time makes heroes</title>
<link rel="stylesheet" href="https://fonts.googleapis.com/css2?family=Open+Sans:wght@700&display=swap">
<style>
  :root {
    --poster-blue: #4f52f6;
    --ink-white: #ffffff;
    --ink-black: #111111;
  }
  html, body {
    margin: 0;
    padding: 0;
    overflow: hidden;
  }
  .poster {
    position: relative;
    width: 847px;
    height: 1200px;
    background: var(--poster-blue);
    font-family: "Open Sans", Arial, sans-serif;
    color: var(--ink-white);
    overflow: hidden;
  }
  .rule {
    position: absolute;
    left: 276px;
    width: 293px;
    background: var(--ink-white);
  }
  .rule--top { top: 176px; height: 11px; }
  .rule--mid { top: 805px; height: 11px; }
  .rule--thin { top: 906px; height: 6px; }
  .quote {
    position: absolute;
    top: 221px;
    left: 0;
    width: 100%;
    margin: 0;
    text-align: center;
    font-size: 61px;
    font-weight: 700;
    line-height: 89.5px;
    letter-spacing: -0.5px;
  }
  .quote span { display: block; }
  .attribution {
    position: absolute;
    top: 845px;
    left: 0;
    width: 100%;
    margin: 0;
    text-align: center;
    font-size: 25px;
    font-weight: 700;
    line-height: 36px;
  }
  .brand-tab {
    position: absolute;
    left: 276px;
    top: 990px;
    width: 293px;
    height: 210px;
  }
  .brand-tab svg {
    position: absolute;
    inset: 0;
  }
  .brand-name {
    position: absolute;
    top: 90px;
    left: 0;
    width: 100%;
    text-align: center;
    color: var(--ink-black);
    font-size: 30px;
    font-weight: 700;
    line-height: 40px;
  }
  .brand-url {
    position: absolute;
    top: 148px;
    left: 0;
    width: 100%;
    text-align: center;
    color: var(--ink-black);
    font-size: 21px;
    font-weight: 700;
  }
</style>
</head>
<body>
<main class="poster">
  <div class="rule rule--top"></div>

  <h1 class="quote">
    <span>Time</span>
    <span>makes</span>
    <span>heroes</span>
    <span>&amp;</span>
    <span>desolves</span>
    <span>celebrities.</span>
  </h1>

  <div class="rule rule--mid"></div>
  <p class="attribution">Martin R. Ellacott</p>
  <div class="rule rule--thin"></div>

  <div class="brand-tab">
    <svg width="293" height="210" viewBox="0 0 293 210" aria-hidden="true">
      <polygon points="0,0 146.5,24 293,0 293,210 0,210" fill="#ffffff"/>
    </svg>
    <div class="brand-name">Hourgala</div>
    <div class="brand-url">www.hourgala-events.ca</div>
  </div>
</main>
</body>
</html>
```